Business card for Full Stable Care Vandorpe

I would like to have me designed an professional business card with my existing logo for my company called : full stable care vandorpe gcv.
I prefer a two sided business card with on the back side only the horses head and the website : fscvandorpe-example.eu
Only one colour shouldbe all right.
The logo must appear in a nic professional way on the business card.

Other suggestion are welcome.

All copy wrights must be released by the designer after we have selected a final design.

Target Market(s)

Equestrian businesses

Industry/Entity Type

Business

Contact Information for Business Card

Laurent Vandorpe
Title: zaakvoerder
Full Stable Care Vandorpe GCV
Molkenweg 47
B - 2820 Bonheiden
België
Phone: + 32 491 68 27 04
Mail: laurent@fscvandorpe-example.eu

Font styles to use
Serif

Requirements
Must have
• My own logo
• See attached files
• Website: fscvandorpe-example.eu

```html
<!DOCTYPE html>
<html lang="nl">
<head>
<meta charset="utf-8">
<title>Full Stable Care Vandorpe – Business Card</title>
<link rel="stylesheet" href="https://fonts.googleapis.com/css2?family=Playfair+Display:wght@700&family=Arimo:wght@400;700&display=swap">
<style>
  :root {
    --backdrop: #2b2b2b;
    --card-light: #ffffff;
    --card-shade: #dcdcdc;
    --band: #0d0d0d;
    --swoosh: #9a9a9a;
    --ink: #111111;
    --name-grey: #6a6a6a;
    --on-band: #ffffff;
  }
  * { margin: 0; padding: 0; box-sizing: border-box; }
  html, body {
    width: 1200px;
    height: 997px;
    overflow: hidden;
    background: var(--backdrop);
  }
  .canvas {
    position: relative;
    width: 1200px;
    height: 997px;
  }
  .card {
    position: absolute;
    left: 320px;
    width: 560px;
    height: 320px;
    border-radius: 24px;
    overflow: hidden;
    background: linear-gradient(160deg, var(--card-light) 0%, #f1f1f1 45%, var(--card-shade) 100%);
    box-shadow: 0 18px 40px rgba(0,0,0,0.55);
  }
  .card--contact { top: 150px; }
  .card--brand { top: 527px; }
  .card__art {
    position: absolute;
    inset: 0;
    width: 100%;
    height: 100%;
  }
  .wordmark {
    display: flex;
    align-items: center;
    gap: 8px;
    font-family: "Playfair Display", Georgia, serif;
    font-weight: 700;
    color: var(--ink);
    white-space: nowrap;
  }
  .wordmark__dot {
    border-radius: 50%;
    background: var(--ink);
    flex: none;
  }
  .card--contact .wordmark {
    position: absolute;
    top: 30px;
    right: 30px;
    font-size: 16px;
  }
  .card--contact .wordmark__dot { width: 12px; height: 12px; }
  .holder {
    position: absolute;
    left: 36px;
    top: 132px;
    font-family: "Arimo", Arial, sans-serif;
  }
  .holder__name {
    font-size: 18px;
    color: var(--name-grey);
    font-weight: 400;
  }
  .holder__title {
    font-size: 14px;
    color: var(--ink);
    font-weight: 700;
    margin-top: 2px;
  }
  .contact-list {
    position: absolute;
    left: 30px;
    top: 226px;
    list-style: none;
    font-family: "Arimo", Arial, sans-serif;
    font-size: 13px;
    color: var(--on-band);
  }
  .contact-list li {
    display: flex;
    align-items: center;
    gap: 10px;
    height: 26px;
  }
  .contact-list svg { width: 18px; height: 18px; flex: none; }
  .card--brand .wordmark {
    position: absolute;
    left: 0;
    right: 0;
    top: 112px;
    justify-content: center;
    font-size: 29px;
  }
  .card--brand .wordmark__dot { width: 20px; height: 20px; }
  .website {
    position: absolute;
    right: 26px;
    bottom: 30px;
    font-family: "Arimo", Arial, sans-serif;
    font-weight: 700;
    font-size: 13px;
    letter-spacing: 2px;
    color: var(--on-band);
  }
</style>
</head>
<body>
<main class="canvas">

  <section class="card card--contact" aria-label="Card front with contact details">
    <svg class="card__art" viewBox="0 0 560 320" preserveAspectRatio="none" aria-hidden="true">
      <path d="M0,186 C190,184 390,136 560,92 L560,110 C380,152 180,200 0,202 Z" fill="var(--swoosh)"/>
      <path d="M0,202 C180,200 380,152 560,110 L560,320 L0,320 Z" fill="var(--band)"/>
    </svg>
    <div class="wordmark"><span class="wordmark__dot"></span>Full Stable Care Vandorpe</div>
    <div class="holder">
      <p class="holder__name">Laurent Vandorpe</p>
      <p class="holder__title">Zaakvoerder</p>
    </div>
    <ul class="contact-list">
      <li>
        <svg viewBox="0 0 18 18" aria-hidden="true"><circle cx="9" cy="9" r="9" fill="#fff"/><path d="M6 4.5 L7.6 4.5 L8.2 6.8 L7.2 7.6 C7.7 8.8 8.8 10 10.2 10.6 L11 9.6 L13.4 10.2 L13.4 11.8 C13.4 12.6 12.7 13.2 11.8 13 C8.4 12.4 5.6 9.6 5 6.2 C4.9 5.2 5.3 4.5 6 4.5 Z" fill="#111"/></svg>
        <span>+ 32 491 68 27 04</span>
      </li>
      <li>
        <svg viewBox="0 0 18 18" aria-hidden="true"><circle cx="9" cy="9" r="9" fill="#fff"/><rect x="4.5" y="5.8" width="9" height="6.4" fill="#111"/><path d="M4.5 5.8 L9 9.4 L13.5 5.8" fill="none" stroke="#fff" stroke-width="0.9"/></svg>
        <span>laurent@fscvandorpe-example.eu</span>
      </li>
      <li>
        <svg viewBox="0 0 18 18" aria-hidden="true"><circle cx="9" cy="9" r="9" fill="#fff"/><path d="M9 4.2 L13.6 8.4 L12.3 8.4 L12.3 13 L10.1 13 L10.1 10.4 L7.9 10.4 L7.9 13 L5.7 13 L5.7 8.4 L4.4 8.4 Z" fill="#111"/></svg>
        <span>Molkenweg 47 B-2899 Heidebeek, België</span>
      </li>
    </ul>
  </section>

  <section class="card card--brand" aria-label="Card back with logo and website">
    <svg class="card__art" viewBox="0 0 560 320" preserveAspectRatio="none" aria-hidden="true">
      <path d="M130,320 C290,292 450,236 560,162 L560,182 C460,252 300,302 185,320 Z" fill="var(--swoosh)"/>
      <path d="M185,320 C300,302 460,252 560,182 L560,320 Z" fill="var(--band)"/>
    </svg>
    <div class="wordmark"><span class="wordmark__dot"></span>Full Stable Care Vandorpe</div>
    <p class="website">www.fscvandorpe-example.eu</p>
  </section>

</main>
</body>
</html>
```